Business Cards Needed For Veterinary Business

Looking for a business card design for a veterinary blood bank. We would like it to be clean and professional on appearance but still warm and inviting. We would like to utilize our logo and similar coloring. We will use our phone number, email, website, employee name, employee title.

We do not want a bunch of animated animal photos but do not need the style to be as clinical as a laboratory or human medical procedure office.

We are looking for some creative ideas to choose from so that we can generate a standout professional business card for our management team to utilize.

Target Market(s)

professionals

Industry/Entity Type

veterinary

Contact Information for Business Card

employee name, employee title, phone number, website URL, email

Font styles to use
Sans Serif

Colors
0054AA
0677BA
7BADD7
CADEEF
E8F1F8
EB3D1F
EC4F4E
F09395
F8D3D4
FCEDEE

Requirements
Nice to have
• creative design
Should not have
• animated photos

```html
<!DOCTYPE html>
<html lang="en">
<head>
<meta charset="utf-8">
<title>Meridian Pet Blood Bank – Business Card</title>
<link rel="stylesheet" href="https://fonts.googleapis.com/css2?family=Montserrat:wght@700;800&family=Roboto:wght@400;500&display=swap">
<style>
  :root {
    --page-bg: #2b2b2b;
    --card-bg: #262626;
    --card-bg-light: #2e2e2e;
    --brand-red: #d81f26;
    --brand-red-deep: #b8191f;
    --brand-blue: #1f56a6;
    --tag-grey: #8a8a8a;
    --text-light: #f2f2f2;
    --shade: #1c1c1c;
  }
  * { box-sizing: border-box; margin: 0; padding: 0; }
  html, body {
    width: 1200px; height: 576px; overflow: hidden;
    background: var(--page-bg);
  }
  .canvas { position: relative; width: 1200px; height: 576px; }

  .card {
    position: absolute; top: 138px; height: 294px;
    border-radius: 8px; overflow: hidden;
    background: linear-gradient(160deg, var(--card-bg-light), var(--card-bg));
  }
  .card--front { left: 102px; width: 484px; }
  .card--back  { left: 596px; width: 481px; }

  /* Brand block */
  .brand { position: absolute; font-family: "Montserrat", sans-serif; text-transform: uppercase; line-height: 1; }
  .brand-name { display: block; font-weight: 800; font-size: 37px; color: var(--brand-red); letter-spacing: 0.5px; }
  .brand-line { display: block; font-weight: 700; font-size: 18.5px; color: var(--brand-blue); margin-top: 3px; letter-spacing: 0.3px; }
  .brand-tag { display: block; font-weight: 700; font-size: 12.5px; color: var(--tag-grey); margin-top: 2px; letter-spacing: 0.6px; }

  .card--front .brand { left: 34px; top: 110px; }
  .card--back .brand { right: 47px; top: 34px; text-align: right; }
  .card--back .brand-tag { color: var(--text-light); }

  .emblem-area {
    position: absolute; left: 282px; top: 10px; width: 180px; height: 276px;
    border-radius: 90px;
    background: radial-gradient(ellipse at 45% 40%, #3a3a3a, var(--shade) 75%);
  }

  /* Back */
  .person-name {
    position: absolute; left: 27px; top: 36px;
    font-family: "Roboto", sans-serif; font-weight: 500;
    font-size: 18px; color: var(--brand-red);
  }
  .person-title {
    position: absolute; left: 27px; top: 60px;
    font-family: "Roboto", sans-serif; font-size: 13px; color: var(--text-light);
  }
  .contact-list {
    position: absolute; left: 27px; top: 109px; list-style: none;
    font-family: "Roboto", sans-serif; font-size: 13px; color: var(--text-light);
  }
  .contact-list li { display: flex; align-items: center; height: 18.5px; }
  .contact-list svg { width: 11px; height: 11px; margin: 0 14px 0 6px; fill: var(--brand-red); }
  .address {
    position: absolute; left: 27px; top: 168px;
    font-family: "Roboto", sans-serif; font-size: 13px; line-height: 15px; color: var(--text-light);
  }
  .pulse-area {
    position: absolute; left: 0; top: 228px; width: 254px; height: 36px;
    background: linear-gradient(90deg, rgba(216,31,38,0.10), rgba(216,31,38,0.22));
  }
  .pets-area {
    position: absolute; left: 254px; top: 118px; width: 227px; height: 176px;
    border-radius: 120px 40px 0 0;
    background: linear-gradient(180deg, var(--brand-red), var(--brand-red-deep));
  }
</style>
</head>
<body>
<main class="canvas">
  <section class="card card--front">
    <div class="brand">
      <span class="brand-name">Meridian</span>
      <span class="brand-line">Pet Blood Bank</span>
      <span class="brand-tag">Transfusion Services</span>
    </div>
    <div class="emblem-area" role="img" aria-label="Embossed blood-drop emblem with pet silhouettes"></div>
  </section>

  <section class="card card--back">
    <div class="person-name">Dana Reyes</div>
    <div class="person-title">Managing Director</div>
    <ul class="contact-list">
      <li><svg viewBox="0 0 12 12"><path d="M2 1h2.5l1 3-1.5 1a6 6 0 0 0 3 3l1-1.5 3 1V11c-5 0-9-4-9-9z"/></svg>555-014-2270</li>
      <li><svg viewBox="0 0 12 12"><path d="M1 2.5h10v7H1z M1.5 3l4.5 3.5L10.5 3" stroke="#262626" stroke-width="0.9"/></svg>dana@meridianpet.example</li>
      <li><svg viewBox="0 0 12 12"><circle cx="6" cy="6" r="5"/><path d="M1 6h10M6 1c-2.5 3-2.5 7 0 10M6 1c2.5 3 2.5 7 0 10" stroke="#262626" stroke-width="0.8" fill="none"/></svg>www.meridianpet.example</li>
    </ul>
    <div class="address">418 Harbor Lane, Eastfield,<br>Riverton, US 204817</div>
    <div class="brand">
      <span class="brand-name">Meridian</span>
      <span class="brand-line">Pet Blood Bank</span>
      <span class="brand-tag">Transfusion Services</span>
    </div>
    <div class="pulse-area" role="img" aria-label="Red heartbeat trace decoration"></div>
    <div class="pets-area" role="img" aria-label="Red silhouette of a dog and a cat"></div>
  </section>
</main>
</body>
</html>
```